We would like a Industrial brouchure design, for OIL and Gas and chemical industry , target customers are Petrochemical refineries, power plants and Petroleum tanker trucks.
this brouchure should have product photos of our main products.
I.E - stainless steel expasnion joints, rubber expansion joints, Fabric expansion joints, Composite hose, hand built rubber hose.
this brouchure is to hand to customers to show them our company capabilities
Design ideas can be taken from our web site - www.korvanite.com.au
Our products are high end engineered products, we supply all of Australia, new Zealand and south east asia and pacific islands
i would like a location map on the brouchure showing our locations.
our locations are -

Perth Western Australia
Port hedland western Australia
Darwin Northen territory
Adelaide - south Australia
Brisbane - Queensland - Australia
Auckland - New zealnd
Singapore
Surabaya - Indonesia
jakarta - indonesia
Ho Chi Min City - Vietnam
balikpapan - indonesia

our comapny logo colors are Black and grey

we would need product photos as well for the following products

Composite hose
stainless steel expansion joints
rubber expasnion joints
Fabric expansion joints
hand biuilt rubber hose
Composite ship to shore petroleum dock hose
stainless braided flexible hose

Target Market(s)

petrochemical industry
refineries, petroleum tanker, power plants, mining

Requirements
Must have
• product photos
• map of where we are located
• high end company impression
Nice to have
• 3 plus pages

```html
<!DOCTYPE html>
<html lang="en">
<head>
<meta charset="utf-8">
<title>Korvanite Brochure Spread</title>
<link href="https://fonts.googleapis.com/css2?family=Oxanium:wght@400;500;600&family=Open+Sans:wght@400&display=swap" rel="stylesheet">
<style>
  :root {
    --backdrop: #c4c4c4;
    --paper: #ffffff;
    --paper-shade: #e2e2e2;
    --ink: #1e1e1e;
    --body-ink: #2c2c2c;
    --band-dark: #2a2a2a;
    --band-light: #8a8a8a;
    --sunset-top: #3b3f63;
    --sunset-mid: #d9793a;
    --sunset-low: #6a2a1e;
    --night-top: #1f3f86;
    --night-mid: #6f9ccf;
    --night-low: #c9d3da;
  }
  * { margin: 0; padding: 0; box-sizing: border-box; }
  html, body { width: 1200px; height: 900px; overflow: hidden; }
  body {
    background: var(--backdrop);
    font-family: "Open Sans", sans-serif;
    color: var(--body-ink);
  }
  .spread {
    position: absolute;
    left: 233px; top: 325px;
    width: 729px; height: 261px;
    display: flex;
  }
  .photo { height: 100%; }
  .photo--refinery-sunset {
    width: 197px;
    background: linear-gradient(170deg, var(--sunset-top) 0%, #8a5a5a 25%, var(--sunset-mid) 45%, #a2452a 65%, var(--sunset-low) 100%);
  }
  .photo--refinery-night {
    width: 202px;
    background: linear-gradient(180deg, var(--night-top) 0%, #2d5aa0 20%, var(--night-mid) 50%, var(--night-low) 75%, #2f6fb8 100%);
  }
  .page { position: relative; height: 100%; }
  .page--intro {
    width: 162px;
    background: linear-gradient(90deg, var(--paper) 78%, var(--paper-shade) 100%);
  }
  .page--products {
    width: 168px;
    background: linear-gradient(90deg, #cfcfcf 0%, #ececec 12%, var(--paper) 35%);
  }
  .block { position: absolute; }
  .page--intro .block { left: 16px; width: 134px; }
  .page--products .block { left: 16px; width: 140px; }
  .heading {
    font-family: "Oxanium", sans-serif;
    font-weight: 500;
    color: var(--ink);
    letter-spacing: 0.03em;
    line-height: 1.35;
  }
  .heading--page { font-size: 7.2px; }
  .heading--section { font-size: 6.2px; margin-bottom: 1px; }
  .body-copy {
    font-size: 4.5px;
    line-height: 6.6px;
  }
  .section-band {
    position: absolute;
    left: 2px; top: 15px;
    width: 151px; height: 14px;
    background: linear-gradient(90deg, var(--band-dark) 0%, #4a4a4a 60%, var(--band-light) 100%);
    color: #ffffff;
    font-family: "Oxanium", sans-serif;
    font-weight: 400;
    font-size: 9px;
    line-height: 14px;
    letter-spacing: 0.06em;
    padding-left: 14px;
  }
  .brand__name {
    font-family: "Oxanium", sans-serif;
    font-weight: 600;
    font-size: 10px;
    letter-spacing: 0.02em;
    color: var(--ink);
  }
</style>
</head>
<body>
  <main class="spread">
    <div class="photo photo--refinery-sunset" role="img" aria-label="Photo of a petroleum tanker truck driving past a refinery at sunset"></div>

    <section class="page page--intro">
      <h2 class="block heading heading--page" style="top:15px">Fluid Transfer Solutions</h2>
      <p class="block body-copy" style="top:34px">We pride ourselves on being flexible and are relentless in finding solutions for you in order to meet your requirements. At Korvanite, we put you first. Our business is efficiently structured so that we can react quickly, be innovative, and provide a reliable fluid transfer solution in a time frame that helps you. Our technical consultants will work with you to determine the requirements and come up with a cost effective solution that improves your operating systems.</p>

      <div class="block" style="top:93px">
        <h3 class="heading heading--section">Servicing the entire Asia Pacific Region</h3>
        <p class="body-copy">Our extensive experience throughout countries such as Indonesia, Vietnam, and Singapore sets us apart from our competitors. This enables us to supply and support the entire Australian and Asia region.</p>
      </div>

      <div class="block" style="top:135px">
        <h3 class="heading heading--section">Quality Service, Experience, and Knowledge</h3>
        <p class="body-copy">Korvanite has an outstanding team with more than 70 years' combined industry experience. Our team understands your needs and can determine the best solution for you. Our highly trained and qualified staff provide high-quality service every time.</p>
      </div>

      <div class="block brand" style="top:198px">
        <span class="brand__name">KORVANITE</span>
      </div>
    </section>

    <section class="page page--products">
      <h2 class="section-band">PRODUCTS</h2>

      <h3 class="block heading heading--section" style="top:45px">Composite Hoses and<br>Assemblies</h3>
      <p class="block body-copy" style="top:67px">Our complete Composite hose range includes a wide selection of hoses that cater for the Petroleum/Oil &amp; Chemical Industries. We also stock a comprehensive range of fitting for these industries in materials such as Steel, Stainless, and Polypropylene. Our Hose &amp; Fittings comply with all the relevant Australian and International standards.</p>

      <h3 class="block heading heading--section" style="top:122px">Metallic Hose and Assemblies</h3>
      <p class="block body-copy" style="top:137px">Our quality Stainless Steel braided hoses can be assembled with almost any connection. The pressure and chemical compatibility of these products make them suitable for a wide range of uses in almost any industry. The hose assemblies are available in Stainless Steel 304, 316 and 321 on request. The hoses are manufactured, assembled and tested in accordance with the relevant ISO 10380 standard.</p>
    </section>

    <div class="photo photo--refinery-night" role="img" aria-label="Photo of an illuminated refinery and storage tanks at dusk"></div>
  </main>
</body>
</html>
```